A book about police officer shootings needs a dynamic cover design

I've almost completed a book on officer involved shootings...a very hot topic today. The title is "R.K.T. Beyond The Silence Fell." (emphasis on "beyond the silence") It details three separate shooting incidents, all within the same law enforcement family.I need a professional looking book cover that helps capture the drama. I attached a file of something I put together that is close, but I am concerned about "readability" and want a more professional look. I included a photo that I took off the internet of a gun being shot. That particular photo can stay or go, or be altered, but I like the perspective of the photo being fired from the person behind it. I wanted the cover to have the characteristics and color of a police uniform, utilizing blues, silvers, and maybe a little gold. I'm concerned about making sure the font and colors are also easy to read. I also will be working on a website design for "Beyond The Silence.Com" once the book hits the market. The back cover will incorporate the same colors, but only be a picture and excerpts from the book. I've included both for your review.

Target Market(s)

Law Enforcement, Christian, Media

Font styles to use
Sans Serif

Requirements
Must have
• A professional and readable appearance, that captures the drama of the topic. All the wording on the sample cover I attached, unless you come up with something better. A gun being fired from the perspective of the officer pulling the trigger. The size of the book will be the standard 6 x 9 in size. "Beyond The Silence" will eventually be my website domain and social media promotion hashtag.
Nice to have
• I would like the cover to incorporate the colors of a police uniform and badge, traditionally, navy blue, silver and some gold.
Should not have
• No police badge with a black band across. Not my topic.

```html
<!DOCTYPE html>
<html lang="en">
<head>
<meta charset="utf-8">
<title>R.K.T. Beyond The Silence Fell — Cover</title>
<link href="https://fonts.googleapis.com/css2?family=Saira+Extra+Condensed:wght@600&family=Montserrat:wght@800&family=Roboto:wght@400&display=swap" rel="stylesheet">
<style>
  :root {
    --bg-deep: #07090b;
    --bg-smoke: #1b1e21;
    --white: #ffffff;
    --blue-top: #3e98df;
    --blue-bottom: #8fd2f5;
    --gold: #f0a53a;
    --flash-core: #fff7e6;
    --sleeve: #1a2433;
  }
  html, body { margin: 0; padding: 0; overflow: hidden; background: var(--bg-deep); }
  .cover {
    position: relative;
    width: 800px; height: 1200px; overflow: hidden;
    background:
      radial-gradient(ellipse 70% 40% at 50% 20%, rgba(60,64,70,.35), transparent 70%),
      radial-gradient(ellipse 60% 30% at 30% 55%, rgba(70,74,80,.25), transparent 70%),
      linear-gradient(180deg, var(--bg-smoke) 0%, var(--bg-deep) 45%, #0c0e10 100%);
  }
  .scene {
    position: absolute; left: 0; top: 500px; width: 800px; height: 700px;
    background:
      radial-gradient(ellipse 14% 11% at 44% 17%, var(--flash-core) 0%, rgba(255,230,190,.85) 40%, transparent 100%),
      radial-gradient(ellipse 32% 17% at 40% 19%, rgba(224,137,74,.75) 0%, rgba(120,60,30,.4) 50%, transparent 100%),
      radial-gradient(ellipse 30% 24% at 60% 70%, rgba(160,112,90,.95) 0%, rgba(120,80,62,.7) 55%, transparent 100%),
      radial-gradient(ellipse 22% 12% at 56% 33%, rgba(190,195,200,.85) 0%, rgba(120,125,130,.5) 60%, transparent 100%),
      linear-gradient(160deg, transparent 60%, var(--sleeve) 85%);
  }
  .type-layer { position: absolute; left: 0; top: 0; width: 800px; height: 1200px; }
  .series { font-family: 'Saira Extra Condensed', sans-serif; font-weight: 600; fill: var(--white); }
  .title-line { font-family: 'Saira Extra Condensed', sans-serif; font-weight: 600; fill: url(#titleBlue); }
  .title-shadow { filter: drop-shadow(0 3px 4px rgba(0,0,0,.6)); }
  .author { font-family: 'Montserrat', sans-serif; font-weight: 800; fill: var(--gold); }
  .tagline, .blurb { position: absolute; margin: 0; white-space: nowrap; font-family: 'Roboto', sans-serif; }
  .tagline { left: 0; width: 800px; text-align: center; top: 470px; font-size: 22px; color: var(--gold); }
  .blurb { font-size: 19px; color: var(--white); text-shadow: 0 1px 3px rgba(0,0,0,.7); }
  .blurb.first { left: 314px; top: 980px; }
  .blurb.second { left: 412px; top: 1014px; }
</style>
</head>
<body>
  <div class="cover">
    <div class="scene" role="img" aria-label="Photo from behind the shooter: two hands gripping a pistol firing, with a bright muzzle flash and smoke against the dark"></div>
    <svg class="type-layer" viewBox="0 0 800 1200" width="800" height="1200">
      <defs>
        <linearGradient id="titleBlue" x1="0" y1="0" x2="0" y2="1">
          <stop offset="0" stop-color="#3e98df"/>
          <stop offset="1" stop-color="#8fd2f5"/>
        </linearGradient>
      </defs>
      <text class="series" x="293" y="164" font-size="137" textLength="200" lengthAdjust="spacingAndGlyphs">R.K.T.</text>
      <g class="title-shadow">
        <text class="title-line" x="100" y="336" font-size="210" textLength="586" lengthAdjust="spacingAndGlyphs">BEYOND THE</text>
        <text class="title-line" x="106" y="444" font-size="126" textLength="576" lengthAdjust="spacingAndGlyphs">SILENCE FELL</text>
      </g>
      <text class="author" x="132" y="1128" font-size="72" textLength="540" lengthAdjust="spacingAndGlyphs">LT. DAN MARLOW</text>
    </svg>
    <p class="tagline">“It will Happen, and it will come out of nowhere...”</p>
    <p class="blurb first">One Law Enforcement Family...</p>
    <p class="blurb second">Three Life-Changing Stories</p>
  </div>
</body>
</html>
```